Responsive, beautiful email sign-up process pages

My client wants to re-imagine their email newsletter sign up process. The funnel currently starts in the first panel of their home page carousel at:

https://thriftbeacon.co.uk/

It is also featured in the right side of the footer.

I would like to start, what could become a full template re-design project by optimising this crucial user journey. I am attaching the screenshots from the current user journey below and it would be great to get some designs that improve on the look and feel.

Thank you,
Gideon

Target Market(s)

People who want to maximise the interest rate they receive on their cash savings.

Industry/Entity Type

Financial Service

Coding

Coded - Design and coding required

Number of Pages Required

4 page

Font styles to use
Sans Serif

Requirements
Must have
• A well designed, responsive design for all of the elements of the user journey funnel that works well on desktop, laptop, tablet and phone. The site is currently using Bootstrap 3.* for the responsive templates, so it would be useful to continue leveraging these libraries, but in a much more visually appealing way.
• It is felt that the current overall site is dull and unprofessional, so we are using this as a way of showing how much better it could be, which should lead to a sitewide "facelift".
Nice to have
• Creative use of css, svg and javascript to optimise the user experience on all target platforms.
Should not have
• Non-responsive designs.

```html
<!DOCTYPE html>
<html lang="en">
<head>
<meta charset="utf-8">
<title>Thrift Beacon – Savings advice</title>
<link href="https://fonts.googleapis.com/css2?family=Open+Sans:wght@400;600;700;800&display=swap" rel="stylesheet">
<style>
:root{
  --orange:#f47b20;
  --orange-dark:#d9650f;
  --ink:#2b2b2b;
  --charcoal:#333436;
  --dark:#262728;
  --grey:#6f6f6f;
  --light:#f1f1f1;
  --line:#dedede;
  --white:#ffffff;
}
*{box-sizing:border-box;margin:0;padding:0}
html,body{width:1200px;height:2740px;overflow:hidden}
body{font-family:"Open Sans",Arial,sans-serif;color:var(--ink);background:var(--white);font-size:13px;line-height:1.5}
.wrap{width:1120px;margin:0 auto;position:relative}
a{color:inherit;text-decoration:none}

/* header */
.site-header{height:56px}
.site-header .wrap{display:flex;align-items:center;height:56px}
.brand{display:flex;align-items:center;gap:10px;font-weight:700;font-size:21px;color:var(--charcoal)}
.brand-dot{width:24px;height:24px;border-radius:50%;background:var(--orange)}
.hotline{margin-left:200px;text-align:center}
.hotline-number{display:flex;align-items:center;gap:8px;font-weight:700;font-size:18px;color:var(--charcoal);line-height:1.3}
.hotline-tag{font-size:9px;font-weight:700;color:var(--orange);letter-spacing:.5px}
.account-links{margin-left:auto;display:flex;gap:18px;font-size:12px;color:var(--grey);align-items:center}
.account-links .login{background:var(--orange);color:var(--white);padding:3px 12px;border-radius:3px}

.main-nav{height:28px;background:var(--dark)}
.main-nav ul{list-style:none;display:flex;height:28px;align-items:center;justify-content:space-between;width:1120px;margin:0 auto}
.main-nav li{color:#d8d8d8;font-size:12px;font-weight:600}
.main-nav li.active{color:var(--orange)}

/* hero */
.hero{height:516px;position:relative;overflow:hidden}
.hero-photo{position:absolute;inset:0;background:linear-gradient(100deg,#8c7868 0%,#b9a58f 45%,#7d8b99 70%,#d5c6b6 100%)}
.hero-panel{position:absolute;left:0;top:0;bottom:0;width:640px;background:linear-gradient(90deg,var(--orange) 70%,rgba(244,123,32,.85) 88%,rgba(244,123,32,0));padding:70px 0 0 80px;color:var(--white)}
.hero h1{font-size:36px;font-weight:400;line-height:1.25;width:440px}
.hero h1 strong{font-weight:800}
.hero-list{list-style:none;margin:22px 0 26px}
.hero-list li{display:flex;align-items:center;gap:10px;font-size:15px;margin-bottom:6px}
.hero-list svg{flex:none}
.hero-input{display:flex;align-items:center;width:320px;height:42px;border-radius:3px;padding:0 14px;color:#999;background:var(--white);margin-bottom:12px}
.hero-button{display:inline-block;background:var(--dark);color:var(--white);padding:11px 24px;border-radius:3px;font-weight:600;font-size:14px}

.hero-tabs{height:36px;display:flex;background:var(--light);border-bottom:1px solid var(--line)}
.hero-tabs li{list-style:none;flex:1;display:flex;align-items:center;justify-content:center;font-size:14px;color:var(--charcoal)}
.hero-tabs li.active{background:var(--charcoal);color:var(--white);font-weight:600}

/* section headings */
.section-title{text-align:center;font-size:26px;font-weight:700;letter-spacing:1px;color:var(--charcoal);line-height:1.3}
.section-title span{color:var(--orange)}
.section-intro{text-align:center;width:760px;margin:10px auto 0;color:var(--grey);font-size:12px}

/* advice cards */
.advice{height:524px;padding-top:34px}
.cards{display:flex;gap:28px;margin-top:26px}
.card{flex:1;background:var(--charcoal);color:var(--white);height:388px;display:flex;flex-direction:column}
.card-photo{height:210px}
.card-photo.a{background:linear-gradient(135deg,#c7b8a6,#8b7b6a)}
.card-photo.b{background:linear-gradient(135deg,#6d7a86,#b7aa98)}
.card-photo.c{background:linear-gradient(135deg,#a9b9c4,#7f6e63)}
.card-body{padding:22px 18px 16px}
.card h3{font-size:15px;font-weight:700}
.card p{font-size:11px;color:#c9c9c9;margin:6px 0 16px}
.btn{display:inline-flex;align-items:center;gap:8px;background:var(--orange);color:var(--white);font-weight:600;border-radius:3px}
.card .btn{font-size:11px;padding:6px 12px}

/* enquiry */
.enquiry{height:140px;padding-top:32px}
.enquiry-bar{height:76px;background:var(--light);border:1px solid var(--line);display:flex;align-items:center;padding:0 40px}
.enquiry-bar p{font-size:22px;color:var(--charcoal)}
.enquiry-bar strong{color:var(--orange)}
.enquiry-bar .btn{margin-left:auto;font-size:15px;padding:12px 30px}

/* start saving */
.start{height:280px;padding-top:14px}
.features{display:flex;justify-content:space-between;margin-top:22px;padding:0 40px}
.feature{width:300px;text-align:center}
.feature-icon{width:96px;height:96px;border-radius:50%;background:var(--orange);margin:0 auto 12px;display:flex;align-items:center;justify-content:center}
.feature h3{font-size:14px;font-weight:700;color:var(--charcoal)}
.feature h3 span{color:var(--orange);text-decoration:underline}
.feature p{font-size:11px;color:var(--grey);margin-top:4px}

/* access + press */
.access-press{height:410px;padding-top:20px}
.access-press .wrap{display:flex;gap:36px}
.access{width:600px;height:370px;background:var(--charcoal);color:var(--white);padding:24px 30px}
.access-head{display:flex;align-items:center;gap:14px;font-size:21px;border-bottom:1px solid #4a4a4a;padding-bottom:16px}
.access-head .ring{width:44px;height:44px;border-radius:50%;background:var(--orange);display:flex;align-items:center;justify-content:center}
.accounts{display:flex;gap:30px;margin-top:18px}
.account{flex:1}
.account h4{font-size:14px;font-weight:700;color:var(--orange)}
.account p{font-size:11px;color:#c6c6c6;margin:4px 0 10px}
.account ul{list-style:none;font-size:11px;color:#e6e6e6}
.account li{margin-bottom:4px;padding-left:12px;position:relative}
.account li::before{content:"";position:absolute;left:0;top:7px;width:5px;height:5px;background:var(--orange);border-radius:50%}
.account .btn{font-size:11px;padding:6px 14px;margin-top:12px}
.press{flex:1;padding-top:6px}
.press h2{font-size:24px;font-weight:700;color:var(--charcoal)}
.press h2 span{color:var(--orange)}
.quote{margin-top:20px;font-size:12px;color:var(--grey);padding-left:16px;border-left:3px solid var(--orange)}
.quote cite{display:block;font-style:normal;font-weight:700;color:var(--orange);font-size:11px;margin-top:8px}

/* press badges */
.badges{height:362px;padding-top:20px}
.badges .wrap{display:flex;justify-content:space-between;border-top:1px solid var(--line);border-bottom:1px solid var(--line);padding:22px 0}
.badge{width:160px;height:56px;background:var(--light);border:1px solid var(--line);border-radius:4px}

/* footer */
.site-footer{height:388px;background:var(--charcoal);color:#cfcfcf}
.footer-main{height:308px;padding-top:46px}
.footer-main .wrap{display:flex;gap:50px}
.footer-col h4{color:var(--white);font-size:16px;font-weight:700;margin-bottom:14px}
.footer-links{width:360px}
.footer-links .cols{display:flex;gap:30px}
.footer-links ul{list-style:none;font-size:12px;line-height:2.1}
.footer-about{width:330px;font-size:12px}
.footer-about p{margin-bottom:12px}
.footer-signup{flex:1;font-size:12px}
.signup-form{display:flex;margin-top:18px}
.signup-form span{flex:1;height:40px;background:var(--white);color:#999;display:flex;align-items:center;padding:0 12px;border-radius:3px 0 0 3px}
.signup-form .btn{border-radius:0 3px 3px 0;padding:0 26px;height:40px;font-size:13px}
.footer-bar{height:80px;background:var(--dark)}
.footer-bar .wrap{display:flex;align-items:center;height:80px;font-size:11px;color:#9a9a9a}
.footer-bar .copy{margin-left:auto}
</style>
</head>
<body>

<header class="site-header">
  <div class="wrap">
    <a class="brand" href="https://thriftbeacon.co.uk/"><span class="brand-dot"></span>Thrift Beacon</a>
    <div class="hotline">
      <div class="hotline-number">
        <svg width="18" height="18" viewBox="0 0 24 24"><path fill="#f47b20" d="M6.6 10.8a15 15 0 0 0 6.6 6.6l2.2-2.2a1 1 0 0 1 1-.25 11.4 11.4 0 0 0 3.6.57 1 1 0 0 1 1 1V20a1 1 0 0 1-1 1A17 17 0 0 1 3 4a1 1 0 0 1 1-1h3.5a1 1 0 0 1 1 1c0 1.25.2 2.45.57 3.6a1 1 0 0 1-.25 1z"/></svg>
        0800 - 555 0147
      </div>
      <div class="hotline-tag">SPEAK DIRECT TO A SAVINGS EXPERT</div>
    </div>
    <nav class="account-links"><a href="#">Help</a><a href="#">Register Now</a><a class="login" href="#">Log In</a></nav>
  </div>
</header>

<nav class="main-nav">
  <ul>
    <li class="active">Home</li><li>Concierge Service</li><li>Best Buy Tables</li><li>Rate Watch</li><li>News and Alerts</li><li>Advice and Guides</li><li>Awards</li><li>Forums</li><li>About Us</li><li>Contact Us</li>
  </ul>
</nav>

<section class="hero">
  <div class="hero-photo" role="img" aria-label="Photo of a smiling woman in a scarf against a city skyline at sunset"></div>
  <div class="hero-panel">
    <h1>Get <strong>FREE</strong> whole of market information:</h1>
    <ul class="hero-list">
      <li><svg width="16" height="16" viewBox="0 0 16 16"><path d="M3 8l3 3 7-7" stroke="#fff" stroke-width="2.2" fill="none"/></svg>Uncompromised Best Buy Tables</li>
      <li><svg width="16" height="16" viewBox="0 0 16 16"><path d="M3 8l3 3 7-7" stroke="#fff" stroke-width="2.2" fill="none"/></svg>Account Monitoring and Alert Services</li>
      <li><svg width="16" height="16" viewBox="0 0 16 16"><path d="M3 8l3 3 7-7" stroke="#fff" stroke-width="2.2" fill="none"/></svg>Access to Savings Experts</li>
    </ul>
    <span class="hero-input">Enter your email address</span>
    <a class="hero-button" href="#">Choose your free services</a>
  </div>
</section>

<ul class="hero-tabs">
  <li>Inheritance Tax</li><li class="active">FREE Information</li><li>Over £100,000 in savings</li>
</ul>

<section class="advice">
  <div class="wrap">
    <h2 class="section-title">SPECIALIST <span>ADVICE</span></h2>
    <p class="section-intro">Thrift Beacon gives savers clear, independent guidance across the whole market so you can choose the right home for your money. Our experts explain every option in plain language and help you keep your savings working harder.</p>
    <div class="cards">
      <article class="card">
        <div class="card-photo a" role="img" aria-label="Photo of an older couple reviewing paperwork with an adviser"></div>
        <div class="card-body">
          <h3>£100,000 PLUS IN SAVINGS?</h3>
          <p>Find out how we can help you spread larger balances safely. Download our free guide.</p>
          <a class="btn" href="#">Would you like to know more? ›</a>
        </div>
      </article>
      <article class="card">
        <div class="card-photo b" role="img" aria-label="Photo of a wealth manager in a meeting"></div>
        <div class="card-body">
          <h3>WEALTH MANAGEMENT</h3>
          <p>Get tailored advice to grow and protect your wealth over the long term with our partners.</p>
          <a class="btn" href="#">Would you like to know more? ›</a>
        </div>
      </article>
      <article class="card">
        <div class="card-photo c" role="img" aria-label="Photo of a family enjoying time outdoors"></div>
        <div class="card-body">
          <h3>TAKE OUR £50 CHALLENGE</h3>
          <p>If you have over £50,000 in savings, we're confident we can improve your savings returns.</p>
          <a class="btn" href="#">Would you like to know more? ›</a>
        </div>
      </article>
    </div>
  </div>
</section>

<section class="enquiry">
  <div class="wrap">
    <div class="enquiry-bar">
      <p>If you have an enquiry call us on: <strong>0800 555 0147</strong></p>
      <a class="btn" href="#">Send us an enquiry ›</a>
    </div>
  </div>
</section>

<section class="start">
  <div class="wrap">
    <h2 class="section-title">START SAVING <span>TODAY</span></h2>
    <p class="section-intro">Open an account in minutes and start earning a better rate on your cash. Every account we list is checked by our team so you can save with confidence.</p>
    <div class="features">
      <div class="feature">
        <div class="feature-icon"><svg width="48" height="48" viewBox="0 0 48 48" fill="none" stroke="#fff" stroke-width="3"><rect x="6" y="10" width="36" height="32" rx="3"/><path d="M6 19h36M15 5v9M33 5v9"/><text x="24" y="37" fill="#fff" stroke="none" font-family="Open Sans, sans-serif" font-size="14" font-weight="700" text-anchor="middle">27</text></svg></div>
        <h3>No Monthly Fees, No Minimums</h3>
        <p>Receive a competitive rate with no monthly fees or minimum balance required to open.</p>
      </div>
      <div class="feature">
        <div class="feature-icon"><svg width="50" height="50" viewBox="0 0 50 50" fill="#fff"><path d="M25 5 5 16v4h40v-4z"/><rect x="9" y="22" width="5" height="16"/><rect x="19" y="22" width="5" height="16"/><rect x="28" y="22" width="5" height="16"/><rect x="37" y="22" width="5" height="16"/><rect x="5" y="40" width="40" height="5"/></svg></div>
        <h3>Links Easily with your Current Bank Accounts <span>Find Out More</span></h3>
        <p>Move money between your accounts quickly and simply whenever you need it.</p>
      </div>
      <div class="feature">
        <div class="feature-icon"><svg width="48" height="48" viewBox="0 0 48 48" fill="none" stroke="#fff" stroke-width="3"><circle cx="24" cy="24" r="18"/><path d="M24 13v11l8 5"/></svg></div>
        <h3>24/7 Account Access!</h3>
        <p>Check balances and manage your savings online at any time, day or night.</p>
      </div>
    </div>
  </div>
</section>

<section class="access-press">
  <div class="wrap">
    <div class="access">
      <div class="access-head">
        <span class="ring"><svg width="22" height="22" viewBox="0 0 24 24" fill="none" stroke="#fff" stroke-width="2.4"><circle cx="12" cy="12" r="9"/><path d="M12 7v5l3 2"/></svg></span>
        When you need access to your money
      </div>
      <div class="accounts">
        <div class="account">
          <h4>Instant Access Account</h4>
          <p>Withdraw whenever you need to with no penalty and earn a steady rate on every pound.</p>
          <ul>
            <li>Up to 1.45% AER variable</li>
            <li>Minimum balance of £1,000</li>
            <li>Maximum balance £1 million</li>
            <li>Manage online or by phone</li>
          </ul>
          <a class="btn" href="#">Learn More</a>
        </div>
        <div class="account">
          <h4>Notice Access Account</h4>
          <p>Give notice before withdrawing and in return earn a higher rate on your savings.</p>
          <ul>
            <li>Up to 1.80% AER variable</li>
            <li>90 day notice period</li>
            <li>Minimum balance of £5,000</li>
            <li>Interest paid monthly</li>
          </ul>
          <a class="btn" href="#">Learn More</a>
        </div>
      </div>
    </div>
    <div class="press">
      <h2>THRIFT BEACON <span>IN THE PRESS</span></h2>
      <blockquote class="quote">
        Thrift Beacon's research into savings rates is one of the most useful resources for anyone looking to make their money work harder. Their best buy tables are clear, honest and free from commission.
        <cite>Nora Pell, Deputy Personal Finance Editor, Ledger Media Group</cite>
      </blockquote>
      <blockquote class="quote">
        For savers with large balances, Thrift Beacon offers a simple way to spread cash across safe accounts and earn a better return without spending hours on research.
        <cite>Nora Pell, Deputy Personal Finance Editor, Ledger Media Group</cite>
      </blockquote>
    </div>
  </div>
</section>

<section class="badges" aria-label="As featured in">
  <div class="wrap">
    <span class="badge"></span><span class="badge"></span><span class="badge"></span><span class="badge"></span><span class="badge"></span><span class="badge"></span>
  </div>
</section>

<footer class="site-footer">
  <div class="footer-main">
    <div class="wrap">
      <div class="footer-col footer-links">
        <h4>Top Savings Accounts</h4>
        <div class="cols">
          <ul><li>High Interest Current Accounts</li><li>Variable Rate ISAs</li><li>Monthly Income</li><li>Easy Access</li></ul>
          <ul><li>Fixed Rate Bonds</li><li>Fixed Rate ISAs</li><li>Children's Accounts</li><li>Notice Accounts</li><li>Regular Savings</li></ul>
        </div>
      </div>
      <div class="footer-col footer-about">
        <h4>We're working for a better deal for savers</h4>
        <p>Thrift Beacon campaigns for fairer treatment of savers and helps thousands of people find better rates every year.</p>
        <p>Find out more about us ›</p>
      </div>
      <div class="footer-col footer-signup">
        <h4>Sign up for our newsletter</h4>
        <p>Stay in the loop with the latest savings news and rate alerts delivered straight to your inbox every week.</p>
        <div class="signup-form"><span>Enter email address</span><a class="btn" href="#">Sign Up</a></div>
      </div>
    </div>
  </div>
  <div class="footer-bar">
    <div class="wrap">
      <span>Terms &amp; Conditions | Privacy Policy | Cookie Policy | Website Security</span>
      <span class="copy">© 2015 Thrift Beacon Ltd</span>
    </div>
  </div>
</footer>

</body>
</html>
```